WordPress Website Design for Multi-Brand Aviation Group (Unified Branding System)

Project Overview:
We are seeking a professional, modern WordPress website design for an aviation-focused umbrella company that owns and operates multiple subsidiary businesses. The goal is to create a cohesive visual system that clearly communicates that each company operates under the same parent organization, while still allowing each brand to maintain a slightly distinct identity.
This is not just a single website design—we are looking for a scalable design framework that can be applied across multiple aviation-related businesses.
Objectives:
- Establish a consistent, recognizable brand identity across all company websites
Clearly communicate the relationship between the parent company and its subsidiaries
-bCreate a clean, high-end corporate aviation aesthetic
- Ensure all designs are SEO-friendly and optimized for performance
- Allow flexibility for future expansion (additional subsidiaries)
- Target Audience:
- Corporate aviation clients
- Charter customers
- Students wishing to receive flight training
- Aircraft owners and operators
- Turbine aircraft training to meet insurance requirements
- Business professionals and high-net-worth individuals
- Aviation industry partners
Design Direction & Style:
We are looking for a premium, professional aviation feel—think clean, modern, and high-trust. The design should reflect the standards of corporate aviation: precision, safety, and sophistication.
Key style notes:
Minimalist but impactful layout
High-quality aviation photography (jets, interiors, operations, global travel)
Subtle motion/interaction (hover effects, transitions)
Clear typography hierarchy for readability and professionalism
Branding Requirements:
Incorporate the primary colors of the parent company logo across all designs
Website Structure (Core Pages):
Design a system that includes:
Home Page with the following links:
- About / Company Overview
- Aircraft Management
- Aircraft Acquisition
- Charter
- Pilot Services
- Trip Support
- Contact Page
Site should further include:
- Mobile-first responsive design
- Fast-loading, performance-optimized layouts
SEO & Technical Considerations:
- Design should support high-level SEO implementation:
- Clean layout structure that translates well to semantic HTML
- Proper heading hierarchy (H1, H2, H3)
- Space for keyword-rich content without clutter
- Optimized image placement (with alt text capability)
- Fast load times (lightweight design approach)
- Compatibility with WordPress SEO plugins (e.g., Yoast or Rank Math)
WordPress Requirements:
- Design should be easily built using WordPress (preferred builders: Elementor, Gutenberg, or similar)
- Reusable templates for scalability across multiple sites
- Easy for non-developers to update text and images
- Modular components (blocks/sections that can be reused across pages and sites)
- Navigation & UX:
- Simple, intuitive navigation
- Sticky header preferred
Style guide including:
- Colors
- Fonts
- Button styles
- Layout system
- Designs similar to high-end corporate aviation, private jet charter, or luxury service brands are preferred—clean, sharp, and premium without being overly flashy.
What We Want to Avoid:
- Overly busy layouts
- Generic templates with no brand identity
- Outdated or “stock” looking aviation designs
- Poor mobile responsiveness
Additional Notes:
We are building a long-term brand system, not just a one-off website. There is potential for ongoing work as we expand additional subsidiary sites.
We value designers who understand branding consistency across multiple business units and can create a scalable, professional system.
Include the attached main company logo "Verdane Aviation Group" and the "Member KTFR" logo on the main page.

```html
<!DOCTYPE html>
<html lang="en">
<head>
<meta charset="utf-8">
<title>Verdane Aviation Group</title>
<link href="https://fonts.googleapis.com/css2?family=Playfair+Display:wght@500;600&family=Poppins:wght@400;500;600;700&family=Great+Vibes&display=swap" rel="stylesheet">
<style>
:root{
  --blue:#0b5cc5;
  --blue-bright:#2f7fe6;
  --navy:#0a1830;
  --ink:#1b1d22;
  --muted:#4a4f58;
  --grey:#f2f2f2;
  --white:#ffffff;
  --black:#050505;
  --star:#e9932a;
  --serif:"Playfair Display", Georgia, serif;
  --sans:"Poppins", Arial, sans-serif;
  --script:"Great Vibes", cursive;
}
*{margin:0;padding:0;box-sizing:border-box}
html,body{width:1200px;height:4996px;overflow:hidden}
body{position:relative;background:var(--white);font-family:var(--sans);color:var(--ink)}
.abs{position:absolute}
.serif-title{font-family:var(--serif);font-weight:500;text-transform:uppercase;letter-spacing:1px;line-height:1.08;color:var(--ink)}
.script-label{font-family:var(--script);color:var(--blue);font-size:22px;display:flex;align-items:center;gap:8px;justify-content:center}
.plane-mark{width:42px;height:14px;color:var(--blue)}
.center-col{left:0;width:1200px;text-align:center}
.connector{position:absolute;left:599px;width:1.5px;background:var(--blue)}

/* HERO */
.hero{top:0;left:0;width:1200px;height:912px;overflow:hidden}
.hero-photo{position:absolute;inset:0;background:
  radial-gradient(ellipse 520px 150px at 600px 640px, rgba(226,160,90,.85), rgba(150,95,45,.35) 55%, transparent 80%),
  radial-gradient(ellipse 140px 120px at 600px 560px, rgba(60,66,76,.9), transparent 75%),
  linear-gradient(180deg,#151a21 0%,#1e242c 30%,#2a2d33 50%,#4a3c2c 68%,#6a4e31 76%,#2b2622 86%,#1a1715 100%)}
.social{top:39px;display:flex;gap:9px;left:132px}
.social span{width:34px;height:34px;border:1.5px solid var(--white);border-radius:50%;display:flex;align-items:center;justify-content:center}
.brand{top:30px;left:450px;width:300px;text-align:center;color:var(--white);font-weight:600}
.brand .word{font-size:30px;letter-spacing:5px;line-height:1}
.brand .sub{font-size:13px;letter-spacing:3px;margin-top:4px}
.phone{top:40px;left:898px;display:flex;align-items:center;gap:10px;color:var(--white);font-weight:700;font-size:18px;letter-spacing:.5px}
.phone .ring{width:32px;height:32px;border:1.5px solid var(--white);border-radius:50%;display:flex;align-items:center;justify-content:center}
.nav-rule{left:132px;width:936px;height:1px;background:rgba(255,255,255,.25)}
.nav{top:120px;left:196px;width:808px;display:flex;justify-content:space-between;font-size:9.5px;font-weight:600;letter-spacing:.8px;color:var(--white)}
.nav-active{top:96px;left:190px;width:44px;height:3px;background:var(--blue-bright)}
.hero-title{top:218px;font-size:38px;color:var(--white)}
.hero-text{top:304px;left:340px;width:520px;text-align:center;color:#e6e8ec;font-size:11.5px;line-height:1.75}
.btn{display:inline-flex;align-items:center;justify-content:center;font-size:9.5px;font-weight:600;letter-spacing:.8px;text-transform:uppercase;border-radius:8px}
.btn-solid{background:var(--blue);color:var(--white)}
.btn-ghost{border:1.5px solid var(--white);color:var(--white)}
.hero-cta1{top:360px;left:450px;width:142px;height:40px}
.hero-cta2{top:360px;left:606px;width:144px;height:40px}
.badges{top:756px;left:148px;display:flex;align-items:center;gap:22px;color:var(--white);font-size:9px;font-weight:600;letter-spacing:.6px}
.badge{display:flex;align-items:center;gap:8px;line-height:1.25}
.badge .chip{width:24px;height:24px;border-radius:50%;border:1.5px solid var(--white)}
.badge-sep{width:1px;height:40px;background:rgba(255,255,255,.5)}
.hero-cut{position:absolute;left:0;top:0}

/* SERVICES GRID */
.grid-title{top:954px;font-size:30px}
.card{position:absolute;width:264px;height:310px;background:var(--white);border-radius:10px;box-shadow:0 4px 18px rgba(0,0,0,.09);text-align:center}
.card .shot{position:absolute;top:4px;left:4px;width:256px;height:208px;border-radius:8px}
.card h3{position:absolute;top:244px;left:0;width:100%;font-family:var(--serif);font-weight:500;font-size:12.5px;letter-spacing:.5px}
.card p{position:absolute;top:268px;left:0;width:100%;font-size:10px;color:var(--muted)}

/* SUBSIDIARY */
.subsidiary{top:1793px;left:0;width:1200px;height:534px;background:var(--grey)}
.sub-title{top:1932px;font-size:30px}
.sub-text{top:2010px;left:340px;width:520px;text-align:center;font-size:10.5px;line-height:1.8;color:var(--muted)}
.units{top:2084px;left:210px;width:780px;height:142px;display:flex}
.unit{flex:1;display:flex;flex-direction:column;align-items:center;justify-content:center;gap:14px;border-right:1px solid #d6d6d6}
.unit:last-child{border-right:0}
.unit svg{width:64px;height:64px}
.unit span{font-family:var(--serif);font-size:11.5px;letter-spacing:.6px}

/* FEATURED */
.feat-title{top:2450px;font-size:30px}
.feat-card{position:absolute;top:2495px;width:462px;height:272px;border-radius:8px;overflow:hidden}
.feat-card .shot{position:absolute;inset:0}
.feat-card .body{position:absolute;left:44px;top:82px;width:190px;color:var(--white)}
.feat-card h3{font-family:var(--serif);font-weight:500;font-size:12px;letter-spacing:.5px;margin-bottom:6px}
.feat-card p{font-size:10.5px;line-height:1.75;color:#e4e6ea}
.feat-card .btn{margin-top:22px;width:120px;height:36px}

/* GLOBAL */
.global{top:2866px;left:0;width:1200px;height:463px;background:var(--navy)}
.map{position:absolute;left:485px;top:52px;width:600px;height:380px;background:
  radial-gradient(ellipse 90px 70px at 22% 45%, rgba(60,120,215,.45), transparent 75%),
  radial-gradient(ellipse 110px 80px at 55% 40%, rgba(60,120,215,.45), transparent 75%),
  radial-gradient(ellipse 120px 90px at 82% 45%, rgba(60,120,215,.4), transparent 75%),
  radial-gradient(ellipse 70px 90px at 32% 78%, rgba(50,100,190,.35), transparent 75%),
  radial-gradient(ellipse 60px 60px at 58% 72%, rgba(50,100,190,.35), transparent 75%),
  linear-gradient(180deg,#0c1d3a,#0a1830)}
.global-label{left:132px;top:96px;display:flex;align-items:center;gap:10px;font-family:var(--serif);color:var(--white);font-size:11px;letter-spacing:.8px}
.global-title{left:132px;top:130px;font-family:var(--serif);font-weight:500;color:var(--white);font-size:31px;line-height:1.15;letter-spacing:1px}
.global-text{left:132px;top:202px;width:290px;font-size:10.5px;line-height:1.8;color:#d7dce6}
.global-note{left:132px;top:316px;display:flex;align-items:center;gap:12px;color:#e4e8ef;font-size:10.5px;line-height:1.6}
.callout{position:absolute;width:122px;padding:8px 10px;border:1px solid rgba(120,160,220,.45);background:rgba(10,24,48,.75);color:#cbd6ea;font-size:8px;line-height:1.5}
.callout b{display:block;font-weight:500;letter-spacing:.8px;margin-bottom:3px;color:var(--white)}
.hub-lines{position:absolute;left:0;top:0}

/* PILOT */
.pilot{top:3329px;left:0;width:1200px;height:462px;background:
  radial-gradient(ellipse 260px 240px at 190px 250px, rgba(175,170,160,.55), transparent 75%),
  radial-gradient(ellipse 200px 230px at 560px 260px, rgba(150,140,128,.45), transparent 75%),
  linear-gradient(90deg,#5c6067 0%,#8a8b8c 30%,#6d6b68 48%,#3c3f45 64%,#25282d 100%)}
.pilot-copy{left:712px;top:3458px;color:var(--white)}
.pilot-copy .script-label{justify-content:flex-start;color:var(--white)}
.pilot-copy .plane-mark{color:var(--white)}
.pilot-copy h2{font-family:var(--serif);font-weight:500;font-size:30px;line-height:1.15;letter-spacing:1px;margin-top:2px}
.pilot-copy ul{list-style:none;margin-top:14px;font-size:10.5px;line-height:1.85}
.pilot-copy .btn{margin-top:18px;width:168px;height:36px}

/* TESTIMONIALS */
.testi-title{top:3940px;font-size:30px}
.testi-text{top:4015px;left:360px;width:480px;text-align:center;font-size:10.5px;line-height:1.8;color:var(--muted)}
.quote{position:absolute;top:4093px;width:363px;height:165px;background:var(--white);border-radius:8px;box-shadow:0 4px 18px rgba(0,0,0,.09);padding:30px 26px}
.quote .stars{color:var(--star);font-size:11px;letter-spacing:2px}
.quote p{margin-top:10px;font-size:10.5px;line-height:1.85;color:var(--muted)}
.quote .who{margin-top:12px;font-family:var(--serif);font-size:10px;font-weight:600;letter-spacing:.3px}

/* FOOTER */
.footer{top:4475px;left:0;width:1200px;height:521px;background:var(--black)}
.cta{top:4353px;left:132px;width:936px;height:248px;background:var(--blue);border-radius:12px}
.cta h2{position:absolute;left:84px;top:66px;font-family:var(--serif);font-weight:500;font-size:29px;line-height:1.17;letter-spacing:1px;color:var(--white)}
.cta p{position:absolute;left:84px;top:140px;width:470px;font-size:10px;line-height:1.85;color:#e6eefb}
.cta .b1{position:absolute;left:609px;top:82px;width:168px;height:36px;background:var(--white);color:var(--blue);border-radius:12px}
.cta .b2{position:absolute;left:609px;top:124px;width:168px;height:36px;border:1.5px solid var(--white);color:var(--white);border-radius:12px}
.foot-brand{left:132px;top:4740px;color:var(--white);font-weight:600}
.foot-brand .word{font-size:54px;letter-spacing:6px;line-height:1}
.foot-brand .sub{font-size:22px;letter-spacing:5px;margin-top:6px}
.foot-col{color:var(--white)}
.foot-col h4{font-family:var(--serif);font-weight:500;font-size:17px;letter-spacing:1px;margin-bottom:16px}
.foot-col li{list-style:none;font-size:10px;line-height:1.9}
.foot-col .k{font-family:var(--serif);font-size:9.5px;letter-spacing:.5px}
.foot-col .v{font-size:12px;letter-spacing:1px;margin-bottom:14px}
.email-box{left:836px;top:4707px;width:210px;height:44px;background:var(--white);border-radius:8px;display:flex;align-items:center;padding-left:16px;font-size:10px;color:#8a8f98}
.signup{left:836px;top:4760px;width:210px;height:44px;background:var(--blue);border-radius:8px;color:var(--white)}
.foot-rule{left:132px;top:4935px;width:936px;height:1px;background:rgba(255,255,255,.18)}
.foot-bottom{top:4958px;left:132px;width:936px;display:flex;justify-content:space-between;font-size:9.5px;color:#d9d9d9}
.foot-bottom nav{display:flex;gap:44px}
.chat{left:1115px;top:4922px;width:38px;height:38px;border-radius:50%;background:var(--white);display:flex;align-items:center;justify-content:center}
</style>
</head>
<body>

<svg width="0" height="0" style="position:absolute">
  <defs>
    <symbol id="plane" viewBox="0 0 42 14"><path d="M1 10 L30 6 L40 1 L36 7 L41 8 L33 9 L24 13 L25 9 L3 12 Z" fill="currentColor"/></symbol>
  </defs>
</svg>

<!-- HERO -->
<header class="abs hero">
  <div class="hero-photo" role="img" aria-label="Twin propeller aircraft on a runway at dusk with landing lights on"></div>
  <svg class="hero-cut" width="1200" height="912" viewBox="0 0 1200 912">
    <polygon points="1200,690 1200,712 0,912 0,880" fill="#0b5cc5"/>
    <polygon points="1200,712 1200,912 0,912" fill="#ffffff"/>
  </svg>
  <div class="abs social">
    <span></span>
    <span><svg width="14" height="11" viewBox="0 0 14 11"><rect x=".5" y=".5" width="13" height="10" rx="1" fill="#fff"/><path d="M1 1l6 5 6-5" stroke="#1e242c" stroke-width="1.2" fill="none"/></svg></span>
    <span></span>
  </div>
  <div class="abs brand"><div class="word">VERDANE</div><div class="sub">AVIATION GROUP</div></div>
  <div class="abs phone"><span class="ring"><svg width="14" height="14" viewBox="0 0 24 24"><path d="M6.6 10.8a15.1 15.1 0 006.6 6.6l2.2-2.2a1 1 0 011-.25 11.4 11.4 0 003.6.57 1 1 0 011 1V20a1 1 0 01-1 1A17 17 0 013 4a1 1 0 011-1h3.5a1 1 0 011 1c0 1.25.2 2.45.57 3.6a1 1 0 01-.25 1z" fill="#fff"/></svg></span>321-555-0148</div>
  <div class="abs nav-rule" style="top:97px"></div>
  <div class="abs nav-active"></div>
  <nav class="abs nav"><span>HOME</span><span>ABOUT</span><span>AIRCRAFT MANAGEMENT</span><span>AIRCRAFT ACQUISITION</span><span>CHARTER</span><span>PILOT SERVICES</span><span>TRIP SUPPORT</span><span>CONTACT</span></nav>
  <div class="abs nav-rule" style="top:151px"></div>
  <h1 class="abs center-col serif-title hero-title">Cinematic Jet Takeoff<br>Aerial Aviation Footage</h1>
  <p class="abs hero-text">A global aviation group delivering aircraft management, charter, and pilot services with unmatched safety and professionalism.</p>
  <a class="abs btn btn-solid hero-cta1">Explore Services</a>
  <a class="abs btn btn-ghost hero-cta2">Request a Quote</a>
  <div class="abs badges">
    <div class="badge"><span>MEMBER KTFR</span></div>
    <div class="badge-sep"></div>
    <div class="badge"><span class="chip"></span><span>SAFETY<br>CERTIFIED</span></div>
    <div class="badge-sep"></div>
    <div class="badge"><span class="chip"></span><span>GLOBAL<br>OPERATIONS</span></div>
  </div>
</header>

<div class="connector" style="top:814px;height:82px"></div>

<!-- SERVICES -->
<div class="abs center-col script-label" style="top:930px">Core Service Overview <svg class="plane-mark"><use href="#plane"/></svg></div>
<h2 class="abs center-col serif-title grid-title">Integrated Aviation<br>Solutions</h2>

<article class="card" style="left:190px;top:1041px"><div class="shot" role="img" aria-label="Businessman looking out at aircraft on the apron" style="background:linear-gradient(90deg,#c9ced4 0%,#a7adb4 45%,#3a3e44 62%,#2a2d32 72%,#c2c7cc 88%,#aeb3b9 100%)"></div><h3>AIRCRAFT MANAGEMENT</h3><p>End-to-end operational oversight</p></article>
<article class="card" style="left:467px;top:1041px"><div class="shot" role="img" aria-label="Advisors reviewing aircraft purchase documents" style="background:linear-gradient(120deg,#d9d4cc 0%,#8c8477 35%,#e7e4de 55%,#3b3d42 80%,#5b5d62 100%)"></div><h3>AIRCRAFT ACQUISITION</h3><p>Expert guidance for aircraft ownership</p></article>
<article class="card" style="left:744px;top:1041px"><div class="shot" role="img" aria-label="Chauffeur greeting a charter client beside a car" style="background:linear-gradient(180deg,#a8624a 0%,#b48570 30%,#d7d9dc 55%,#3a3d44 75%,#8e9197 100%)"></div><h3>CHARTER SERVICES</h3><p>Private aviation on demand</p></article>
<article class="card" style="left:190px;top:1371px"><div class="shot" role="img" aria-label="Uniformed pilot standing in an airport terminal" style="background:linear-gradient(90deg,#d3d9e0 0%,#9aa4ae 30%,#1c2028 45%,#1a1e26 62%,#b9c1ca 78%,#dfe4e9 100%)"></div><h3>PILOT SERVICES</h3><p>Certified pilots for all aircraft types</p></article>
<article class="card" style="left:467px;top:1371px"><div class="shot" role="img" aria-label="Travelers receiving trip assistance at the airport" style="background:linear-gradient(90deg,#6f6a66 0%,#d1ccc4 30%,#b58a4e 55%,#c9a46a 65%,#7d7670 100%)"></div><h3>TRIP SUPPORT</h3><p>Global logistics and flight planning</p></article>
<article class="card" style="left:744px;top:1371px"><div class="shot" role="img" aria-label="Team reviewing compliance documents at a table" style="background:linear-gradient(90deg,#4a4d53 0%,#e3e5e8 30%,#2f333a 55%,#d8cfc4 80%,#b8bcc2 100%)"></div><h3>TRAINING &amp; COMPLIANCE</h3><p>Insurance-ready pilot training programs</p></article>

<!-- SUBSIDIARY -->
<section class="abs subsidiary"></section>
<div class="connector" style="top:1700px;height:177px"></div>
<div class="abs center-col script-label" style="top:1902px">Parent · Subsidiary Structure <svg class="plane-mark"><use href="#plane"/></svg></div>
<h2 class="abs center-col serif-title sub-title">One Group. Multiple<br>Aviation Solutions.</h2>
<p class="abs sub-text">Verdane Aviation Group operates a network of specialized aviation companies, each focused on delivering excellence in its domain while aligned under a unified corporate standard.</p>
<div class="abs units">
  <div class="unit"><svg viewBox="0 0 64 64" fill="none" stroke="#1b1d22" stroke-width="2"><circle cx="32" cy="32" r="18"/><circle cx="32" cy="32" r="10" stroke="#0b5cc5"/><path d="M32 6v8M32 50v8M6 32h8M50 32h8M13 13l6 6M45 45l6 6M51 13l-6 6M19 45l-6 6"/></svg><span>MANAGEMENT</span></div>
  <div class="unit"><svg viewBox="0 0 64 64" fill="none" stroke="#1b1d22" stroke-width="2"><rect x="12" y="10" width="34" height="46" rx="2"/><path d="M20 22h18M20 30h18M20 38h12"/><path d="M52 14L34 46l-2 6 5-4 18-32z" stroke="#0b5cc5"/></svg><span>CHARTER</span></div>
  <div class="unit"><svg viewBox="0 0 64 64" fill="none" stroke="#1b1d22" stroke-width="2"><rect x="16" y="6" width="36" height="24"/><path d="M24 24v-6M32 24v-10M40 24v-4" stroke="#0b5cc5"/><circle cx="14" cy="40" r="5"/><circle cx="32" cy="40" r="5"/><circle cx="50" cy="40" r="5"/><path d="M6 58c0-6 4-10 8-10s8 4 8 10M24 58c0-6 4-10 8-10s8 4 8 10M42 58c0-6 4-10 8-10s8 4 8 10" stroke="#0b5cc5"/></svg><span>TRAINING</span></div>
  <div class="unit"><svg viewBox="0 0 64 64" fill="none" stroke="#1b1d22" stroke-width="2"><path d="M8 38l16-16 10 10-16 16z" fill="#0b5cc5" stroke="#0b5cc5"/><path d="M34 32l14-14 8 8-16 16-8-2z" fill="#0b5cc5" stroke="#0b5cc5"/><path d="M32 6v8M20 10l4 6M44 10l-4 6"/></svg><span>SUPPORT</span></div>
  <div class="unit"><svg viewBox="0 0 64 64" fill="none" stroke="#1b1d22" stroke-width="2"><rect x="20" y="6" width="10" height="10" fill="#0b5cc5" stroke="#0b5cc5"/><rect x="34" y="6" width="10" height="10" fill="#0b5cc5" stroke="#0b5cc5"/><path d="M6 30l12-8 10 6 8-6 10 2 12 8M12 40l10 10 6-2 6 6 6-4 6 2 8-10"/></svg><span>ACQUISITION</span></div>
</div>

<!-- FEATURED -->
<div class="abs center-col" style="top:2420px"><svg class="plane-mark"><use href="#plane"/></svg></div>
<h2 class="abs center-col serif-title feat-title">Featured Services</h2>
<article class="feat-card" style="left:132px"><div class="shot" role="img" aria-label="Executive working on a laptop inside a private jet cabin" style="background:radial-gradient(ellipse 90px 120px at 78% 35%, rgba(230,220,205,.55), transparent 75%),linear-gradient(90deg,#0a0b0d 0%,#17171a 40%,#4a3f36 62%,#8a7c6c 80%,#5e554d 100%)"></div><div class="body"><h3>AIRCRAFT MANAGEMENT</h3><p>Comprehensive management solutions that ensure safety, reliability and value.</p><a class="btn btn-solid">Learn More</a></div></article>
<article class="feat-card" style="left:605px"><div class="shot" role="img" aria-label="Jet cabin window overlooking a city skyline" style="background:radial-gradient(ellipse 110px 80px at 70% 38%, rgba(150,170,190,.75), rgba(90,105,120,.4) 60%, transparent 85%),linear-gradient(90deg,#0c0d10 0%,#1b1c20 45%,#3f454d 70%,#24272c 100%)"></div><div class="body"><h3>PRIVATE CHARTER</h3><p>Experience seamless, luxury travel anywhere in the world with our bespoke charter services.</p><a class="btn btn-solid">Book Charter</a></div></article>

<div class="connector" style="top:2817px;height:91px;z-index:2"></div>

<!-- GLOBAL -->
<section class="abs global">
  <div class="map" role="img" aria-label="World map with glowing operation hubs"></div>
  <svg class="hub-lines" width="1200" height="463" viewBox="0 0 1200 463">
    <g stroke="rgba(140,180,240,.7)" stroke-width="1">
      <line x1="560" y1="112" x2="560" y2="226"/>
      <line x1="792" y1="112" x2="792" y2="210"/>
      <line x1="990" y1="120" x2="990" y2="248"/>
      <line x1="830" y1="343" x2="830" y2="268"/>
    </g>
    <g fill="#5da2ff">
      <circle cx="560" cy="226" r="3"/><circle cx="792" cy="210" r="3"/><circle cx="990" cy="248" r="3"/><circle cx="830" cy="268" r="3"/>
    </g>
  </svg>
  <div class="abs global-label">WORLDWIDE OPERATIONS <svg class="plane-mark" style="color:#fff"><use href="#plane"/></svg></div>
  <h2 class="abs global-title">GLOBAL REACH.<br>LOCAL EXPERTISE.</h2>
  <p class="abs global-text">Verdane Aviation Group delivers world-class aviation services across the globe. Our teams operate with precision, compliance, and local expertise in every region we serve.</p>
  <div class="abs global-note"><svg width="38" height="38" viewBox="0 0 38 38"><circle cx="19" cy="19" r="18" fill="#fff"/><g fill="none" stroke="#0a1830" stroke-width="1.4"><circle cx="19" cy="19" r="11"/><ellipse cx="19" cy="19" rx="5" ry="11"/><path d="M8 19h22M10 13h18M10 25h18"/></g></svg><span>Operating globally with precision and<br>compliance in every region</span></div>
  <div class="callout" style="left:508px;top:54px"><b>NORTH AMERICA</b>Strategic operations across the U.S., Canada, and Latin America.</div>
  <div class="callout" style="left:739px;top:54px"><b>EUROPE</b>Extensive coverage with local expertise and global standards.</div>
  <div class="callout" style="left:952px;top:62px"><b>ASIA</b>Expanding services throughout Asia with unmatched reliability.</div>
  <div class="callout" style="left:805px;top:343px"><b>MIDDLE EAST</b>A strong presence in the heart of global aviation operations.</div>
</section>

<!-- PILOT -->
<section class="abs pilot" role="img" aria-label="Pilots beside a light aircraft in a hangar"></section>
<div class="abs pilot-copy">
  <div class="script-label">Pilot &amp; Training <svg class="plane-mark"><use href="#plane"/></svg></div>
  <h2>CERTIFIED AVIATION<br>EXPERTISE</h2>
  <ul><li>Pilot recruitment</li><li>Training programs</li><li>Insurance compliance readiness</li><li>Simulator training</li></ul>
  <a class="btn btn-solid">Explore Pilot Services</a>
</div>

<div class="connector" style="top:3793px;height:85px"></div>

<!-- TESTIMONIALS -->
<div class="abs center-col script-label" style="top:3906px">Testimonials <svg class="plane-mark"><use href="#plane"/></svg></div>
<h2 class="abs center-col serif-title testi-title">Trusted by Aviation<br>Professionals Worldwide</h2>
<p class="abs testi-text">We proudly serve corporate aviation clients, aircraft owners, and charter users with uncompromising safety, precision, and service excellence.</p>
<article class="quote" style="left:229px"><div class="stars">★★★★★</div><p>Verdane Aviation Group consistently delivers world-class aircraft management with complete professionalism and reliability.</p><div class="who">— DANIEL WHITFORD, CORPORATE AVIATION CLIENT</div></article>
<article class="quote" style="left:607px"><div class="stars">★★★★★</div><p>“Their team understands every detail of aircraft ownership and makes operations completely seamless.”</p><div class="who">— ELENA MARSH, AIRCRAFT OWNER</div></article>

<!-- FOOTER -->
<footer class="abs footer"></footer>
<section class="abs cta">
  <h2>READY TO ELEVATE YOUR<br>AVIATION EXPERIENCE?</h2>
  <p>Partner with a trusted aviation group dedicated to precision, safety, and excellence in every flight. Whether you are looking for aircraft management, charter services, or pilot support, our team is ready to deliver tailored solutions that meet your highest expectations.</p>
  <a class="btn b1">Request a Consultation</a>
  <a class="btn b2">Contact Our Team</a>
</section>

<div class="abs foot-brand"><div class="word">VERDANE</div><div class="sub">AVIATION GROUP</div></div>
<div class="abs foot-col" style="left:508px;top:4712px"><h4>LINKS</h4><ul><li>Home</li><li>About</li><li>Aircraft Management</li><li>Aircraft Acquisition</li><li>Charter</li><li>Pilot Services</li><li>Trip Support</li><li>Contact</li></ul></div>
<div class="abs foot-col" style="left:667px;top:4712px"><h4>CONTACT</h4><div class="k">PHONE:</div><div class="v">321-555-0148</div><div class="k">EMAIL:</div><div class="v">INFO@VERDANEAVIATION.COM</div></div>
<div class="abs email-box">✉&nbsp; Enter email Address</div>
<a class="abs btn signup">Sign Up</a>
<div class="abs foot-rule"></div>
<div class="abs foot-bottom"><span>© 2026 Verdane All Rights Reserved</span><nav><span>Copyright</span><span>Privacy Policy</span><span>Terms</span></nav></div>
<div class="abs chat"><svg width="20" height="18" viewBox="0 0 20 18"><path d="M2 2h16v10H8l-4 4v-4H2z" fill="#0a1830"/><circle cx="7" cy="7" r="1.2" fill="#fff"/><circle cx="10" cy="7" r="1.2" fill="#fff"/><circle cx="13" cy="7" r="1.2" fill="#fff"/></svg></div>

</body>
</html>
```